[Green Press + Juice Bar] Digital Menu Boards (2)

We need designs for our digital menu screens. Dimensions are 1080 x 1920 (9:16). Screens are in portrait mode–2 of them. They will be side by side so designs should be cohesive. We'll need the (Adobe) source files to be able to easily edit in the future.

Check out our Instagram (@pulpwell) to see current brand imagery for inspiration. Please disregard our current website design as it shows our old branding. Visit our Tastemap page to get a feel of the store flow in which the menu boards will be displayed: https://www.tastemap.example/biz/pulpwell-chicago-6

See "Larkfield Menu" attachment for content that will be incorporated into the design for 2 screens.

See "Cleanse Brochure" attachment to see current material we are using to promote our cleansing program. We would like to designate a portion of our menu to promote cleanse options, depending on how much room is available.

Also attached is a photo of our current, static menu board.

We've attached photos of color palettes we like.

Target Market(s)

Health-conscious individuals, healthy moms, fitness gurus, professionals

Industry/Entity Type

Health And Wellness

Font styles to use
Serif
Sans Serif

Colors

Designer to choose colors to be used in the design.

Requirements
Must have
• We need designs for our digital menu screens. Dimensions are 1080 x 1920 (9:16). Screens are in portrait mode–2 of them. We'll need the (Adobe) source files to be able to easily edit in the future. To ensure the sizing of the outputted file is correct and spaced correctly, send us a test file to test on our TV.
Nice to have
• Ideally, the menu will reflect current branding with font usage of one or more of the following:
• FuturaStd-Bold
• Desiderata-Regular
• Wisdom Script
• Bernier Typeface
• Swistblnk Banthers
• Hanley
• If there is space, we'd like to have space to roll a photo/video slideshow on the menu.

```html
<!DOCTYPE html>
<html lang="en">
<head>
<meta charset="utf-8">
<title>Green Press + Juice Bar — Larkfield Menu</title>
<link rel="stylesheet" href="https://fonts.googleapis.com/css2?family=Bebas+Neue&family=Lobster&display=swap">
<style>
  :root {
    --teal: #1c9d8f;
    --teal-deep: #157d72;
    --ink: #0e3f3a;
    --lime: #c9e594;
    --lime-box: #c6e497;
    --yellow: #f2e45e;
    --white: #ffffff;
  }
  * { margin: 0; padding: 0; box-sizing: border-box; }
  html, body { width: 676px; height: 1200px; overflow: hidden; background: var(--teal); }
  .menu-board {
    position: relative; width: 676px; height: 1200px; overflow: hidden;
    background: var(--teal); color: var(--white);
    font-family: "Bebas Neue", "Oswald", sans-serif;
  }
  .column-rule { position: absolute; left: 380px; top: 30px; width: 2px; height: 1140px; background: var(--white); }
  .script-heading { font-family: "Lobster", cursive; font-weight: 400; color: var(--white); position: absolute; font-size: 52px; line-height: 1; }
  .script-heading .size-note { font-family: "Bebas Neue", sans-serif; font-size: 30px; letter-spacing: 1px; }
  .bowl { position: absolute; left: 36px; width: 340px; }
  .bowl-title { display: flex; align-items: center; gap: 12px; margin-bottom: 2px; }
  .bowl-name { background: var(--lime); color: var(--white); font-size: 23px; letter-spacing: 1px; padding: 2px 8px 0; line-height: 25px; }
  .price { color: var(--yellow); font-size: 23px; letter-spacing: 1px; }
  .ingredients { font-size: 14.5px; line-height: 22.8px; letter-spacing: 1px; white-space: nowrap; }
  .ingredients b { font-weight: 400; color: var(--yellow); }
  .keto-note { color: var(--yellow); font-size: 23px; line-height: 27px; letter-spacing: 1px; margin-bottom: 6px; }
  .build-box { position: absolute; left: 40px; top: 877px; width: 312px; height: 305px; background: var(--lime-box); color: var(--teal-deep); padding: 14px 22px; }
  .build-title { font-family: "Lobster", cursive; font-weight: 400; font-size: 30px; line-height: 34px; }
  .build-title .build-price { font-family: "Bebas Neue", sans-serif; color: var(--white); font-size: 28px; }
  .steps { list-style: none; margin-top: 8px; }
  .steps li { display: flex; gap: 12px; font-size: 15px; line-height: 25.5px; letter-spacing: 0.8px; }
  .steps .step-no { color: var(--white); white-space: nowrap; }
  .steps .step-text { color: var(--ink); white-space: nowrap; }
  .side-item { position: absolute; left: 408px; width: 260px; }
  .side-name { font-weight: 400; font-size: 23px; line-height: 30px; letter-spacing: 1px; }
  .side-name .price, .side-name .note { color: var(--yellow); font-size: 14px; }
  .note { color: var(--yellow); font-size: 14px; line-height: 18px; letter-spacing: 0.8px; }
  .cleanse-rule { position: absolute; left: 412px; top: 952px; width: 204px; height: 2px; background: var(--white); }
  .cleanse-title { position: absolute; left: 408px; top: 1000px; font-weight: 400; font-size: 21px; line-height: 29px; letter-spacing: 1px; }
  .cleanse-notes { position: absolute; left: 408px; top: 1068px; font-size: 10px; line-height: 17.5px; letter-spacing: 0.5px; white-space: nowrap; }
</style>
</head>
<body>
<main class="menu-board">
  <div class="column-rule"></div>

  <h1 class="script-heading" style="left:36px; top:16px;">Bowls <span class="size-note">(20oz)</span></h1>

  <section class="bowl" style="top:105px;">
    <div class="bowl-title"><span class="bowl-name">Matcha Bowl</span><span class="price">12.5</span></div>
    <p class="ingredients"><b>Base:</b> Fresh-cracked coconut water, coconut meat,<br>banana, spinach, Medjool dates,<br>tocotrienols, maca, matcha, spirulina.<br><b>Toppings:</b> Hemp seeds, blueberries, cacao nibs,<br>coconut shreds, kiwi, pomegranate seeds, banana,<br>bee pollen, mint sprig.</p>
  </section>

  <section class="bowl" style="top:300px;">
    <div class="bowl-title"><span class="bowl-name">Ruby Orchard</span><span class="price">12</span></div>
    <p class="ingredients"><b>Base:</b> Acai, fresh-pressed apple juice, cherries,<br>banana, strawberry, pomegranate,<br><b>Toppings:</b> Seasonal berries, banana, sprouted almond<br>butter, coconut shreds,<br>goji berries, bee pollen, housemade coconut whip,<br>housemade raw granola, local honey.</p>
  </section>

  <section class="bowl" style="top:492px;">
    <div class="bowl-title"><span class="bowl-name">Cocoa Jungle Crunch</span><span class="price">12</span></div>
    <p class="ingredients"><b>Base:</b> Acai, housemade almond milk, bananas,<br>blueberries, peanut butter, Medjool dates<br><b>Toppings:</b> Housemade raw granola, raw chocolate<br>hearts, peanut butter, raw cacao<br>drizzle, banana, dried banana chips, cacao nibs,<br>local honey, bee pollen.</p>
  </section>

  <section class="bowl" style="top:688px;">
    <div class="bowl-title"><span class="bowl-name">Keto Bowl</span><span class="price">13 (under</span></div>
    <p class="keto-note">15 net carbs)</p>
    <p class="ingredients"><b>Base:</b> Acai, housemade almond milk, coconut meat,<br>avocado, blueberries, cauliflower,<br>pineapple, sprouted almond butter, xylitol.<br><b>Toppings:</b> Seasonal berries, coconut shreds, bee<br>pollen, hemp seeds, mulberries, chia seeds.</p>
  </section>

  <section class="build-box">
    <h2 class="build-title">Build Your<br>Own Bowl <span class="build-price">- $12.5</span></h2>
    <ol class="steps">
      <li><span class="step-no">Step 1:</span><span class="step-text">Start with your liquid- almond<br>milk, apple juice, coconut water</span></li>
      <li><span class="step-no">Step 2:</span><span class="step-text">Choose up to 2 fruits/veggies<br>(all bowls include banana)</span></li>
      <li><span class="step-no">Step 3:</span><span class="step-text">Choose up to 2 superfood add-ins</span></li>
      <li><span class="step-no">Step 4:</span><span class="step-text">Choose up to 4 superfood toppings</span></li>
      <li><span class="step-no">Step 5:</span><span class="step-text">Choose a sweetener (Medjool dates,<br>local honey, xylitol)</span></li>
    </ol>
  </section>

  <h1 class="script-heading" style="left:408px; top:22px;">Bites</h1>

  <section class="side-item" style="top:101px;">
    <h3 class="side-name">Hot oatmeal +<br>seasonal fruit<br>+ superfood toppings <span class="price">7.5</span></h3>
    <p class="ingredients">(Served until 10:30am).</p>
  </section>

  <section class="side-item" style="top:233px;">
    <h3 class="side-name">Avocado Toast</h3>
    <p class="note">(2 slices 8.5/1 slice 4.5)</p>
    <p class="ingredients">Sprouted Harvest 7 bread, avocado,<br>pomegranate, fig, rosemary.</p>
  </section>

  <section class="side-item" style="top:345px;">
    <h3 class="side-name">Orange Cacao Toast</h3>
    <p class="note">(2 slices 8.5/<br>1 slice 4.5) *seasonal*</p>
    <p class="ingredients">Sprouted Harvest cinnamon raisin<br>bread, sprouted almond butter, orange,<br>cacao nibs, local honey, basil.</p>
  </section>

  <h1 class="script-heading" style="left:412px; top:534px;">Soups</h1>

  <section class="side-item" style="top:608px;">
    <h3 class="side-name">Broccoli “Cheddar” Soup</h3>
    <p class="note">16oz (dairy free)</p>
    <p class="ingredients">Red pepper, carrot, cashew, spring onion,<br>lemon, maple, nutritional yeast, pink<br>salt, chili powder, garlic powder, broccoli.</p>
  </section>

  <section class="side-item" style="top:743px;">
    <h3 class="side-name">Veggie Soup with<br>sprouted lentil <span class="note">16oz</span></h3>
    <p class="ingredients">Leek, kale, celery, red pepper,<br>green onion, liquid aminos, fresh ginger,<br>fresh garlic, lemon, salt, pepper,<br>cumin, turmeric, sprouted lentils.</p>
  </section>

  <div class="cleanse-rule"></div>
  <h3 class="cleanse-title">Signature Juice and<br>Smoothie Cleanses</h3>
  <p class="cleanse-notes">*Available at 65/day with nationwide<br>delivery available.<br>*Choose from 5 different signature cleanses<br>available in 1, 3, 5 or 7 day packages<br>*Reboot your body by providing a digestive<br>vacation while refocusing the mind</p>
</main>
</body>
</html>
```